Business Card Design

I am selling Cruelty Free/not tested on animal products.
Ideally I would like pictures of rabbits/guinea pigs/Beagle(dog)/rat/mice, as these are the main creatures that are tested on.
Background of card Earth, clouds or rainbow.
Yes I am an animal activist.
My favorite colours are purple and green.

Reason: havent got the perfect design as yet

Industry/Entity Type

Business

Contact Information for Business Card

GENTLY BY NATURE
Cruelty Free Products
Norma Faldt
0492 837 514

```html
<!DOCTYPE html>
<html lang="en">
<head>
<meta charset="utf-8">
<title>Gently By Nature – Business Card Options</title>
<link rel="stylesheet" href="https://fonts.googleapis.com/css2?family=Titan+One&family=Della+Respira&family=Arimo&display=swap">
<style>
  :root {
    --board: #ebeceb;
    --ink: #333333;
    --white: #ffffff;
    --sky-top: #86c9ec;
    --sky-bottom: #e6f5fc;
    --magenta: #d9247e;
    --sage: #a0ce94;
    --forest: #238736;
    --plum: #a0377a;
    --fur-brown: #9b6a3f;
    --fur-light: #e3cdb4;
    --fur-grey: #8d8476;
    --fur-pale: #d8c5ad;
  }
  * { box-sizing: border-box; margin: 0; padding: 0; }
  html, body {
    width: 1111px; height: 1200px; overflow: hidden;
    background: var(--board);
  }
  .sheet { position: relative; width: 1111px; height: 1200px; }
  .option-number {
    position: absolute;
    font-family: "Arimo", sans-serif;
    font-size: 30px; color: var(--ink);
  }
  .option-number--one { left: 102px; top: 166px; }
  .option-number--two { left: 121px; top: 643px; }

  .card {
    position: absolute;
    width: 718px; height: 425px;
    border-radius: 36px;
    overflow: hidden;
    box-shadow: 0 10px 22px rgba(0,0,0,0.28);
  }
  .card--sky { left: 190px; top: 128px;
    background: radial-gradient(ellipse at 45% 60%, var(--sky-bottom) 0%, var(--sky-top) 80%); }
  .card--white { left: 196px; top: 625px; background: var(--white); }

  .rainbow-art {
    position: absolute; left: 280px; top: 0;
    width: 438px; height: 227px;
    border-top-right-radius: 36px;
  }
  .card--sky .rainbow-art {
    background: linear-gradient(200deg, rgba(163,55,139,0.55) 0%, rgba(255,229,0,0.45) 45%, rgba(227,30,36,0.35) 75%, rgba(134,201,236,0) 100%);
  }
  .card--white .rainbow-art {
    background: linear-gradient(200deg, rgba(229,154,199,0.5) 0%, rgba(255,243,138,0.45) 45%, rgba(245,163,165,0.35) 75%, rgba(255,255,255,0) 100%);
  }

  .photo { position: absolute; border-radius: 40px; z-index: 2; }
  .photo--beagle { left: 42px; top: 50px; width: 213px; height: 214px;
    background: radial-gradient(ellipse at 50% 40%, var(--fur-light) 0%, var(--fur-brown) 70%, rgba(155,106,63,0.6) 100%); }
  .photo--small-animals { left: 268px; top: 82px; width: 357px; height: 168px;
    background: linear-gradient(90deg, var(--fur-grey) 0%, var(--fur-pale) 45%, #e9a860 62%, var(--fur-grey) 85%); }

  .brand-band {
    position: absolute; left: 0; top: 227px;
    width: 100%; height: 119px;
    text-align: center;
    z-index: 1;
  }
  .card--sky .brand-band { background: var(--magenta); }
  .card--white .brand-band { background: var(--forest); }

  .brand-name {
    display: block;
    margin-top: 38px;
    font-family: "Titan One", sans-serif;
    font-size: 38px; letter-spacing: 1px;
    color: var(--white);
    line-height: 1;
  }
  .card--sky .brand-name { -webkit-text-stroke: 1px #5a1a3a; }
  .card--white .brand-name { -webkit-text-stroke: 1.2px var(--plum); }
  .tagline {
    display: block;
    margin-top: 2px;
    font-family: "Della Respira", serif;
    font-size: 29px; color: var(--white);
    line-height: 1.1;
  }

  .contact-band {
    position: absolute; left: 0; top: 346px;
    width: 100%; height: 79px;
    display: flex; align-items: center; justify-content: center; gap: 20px;
    font-family: "Della Respira", serif;
  }
  .card--sky .contact-band { background: var(--sage); color: var(--ink); }
  .card--white .contact-band { color: var(--plum); }
  .contact-name { font-size: 25px; }
  .contact-phone { font-size: 29px; display: flex; align-items: center; gap: 4px; }
  .phone-icon { width: 20px; height: 22px; fill: currentColor; }
</style>
</head>
<body>
<main class="sheet">
  <span class="option-number option-number--one">1</span>
  <span class="option-number option-number--two">2</span>

  <section class="card card--sky">
    <div class="rainbow-art" role="img" aria-label="Illustration of a bright rainbow arching across the sky"></div>
    <div class="photo photo--beagle" role="img" aria-label="Photo of a beagle puppy lying down"></div>
    <div class="photo photo--small-animals" role="img" aria-label="Photo of a rabbit, a guinea pig and a mouse in a row"></div>
    <div class="brand-band">
      <span class="brand-name">GENTLY BY NATURE</span>
      <span class="tagline">Cruelty Free Products</span>
    </div>
    <div class="contact-band">
      <span class="contact-name">Norma Faldt</span>
      <span class="contact-phone">
        <svg class="phone-icon" viewBox="0 0 20 22" aria-hidden="true"><path d="M5 1 L8 6 L6 8 C7 11 9 14 12 16 L14 14 L19 17 L17 21 C9 21 1 12 1 4 Z"/></svg>
        0492 837 514
      </span>
    </div>
  </section>

  <section class="card card--white">
    <div class="rainbow-art" role="img" aria-label="Illustration of a pastel rainbow arching across the top"></div>
    <div class="photo photo--beagle" role="img" aria-label="Photo of a beagle puppy lying down"></div>
    <div class="photo photo--small-animals" role="img" aria-label="Photo of a rabbit, a guinea pig and a mouse in a row"></div>
    <div class="brand-band">
      <span class="brand-name">GENTLY BY NATURE</span>
      <span class="tagline">Cruelty Free Products</span>
    </div>
    <div class="contact-band">
      <span class="contact-name">Norma Faldt</span>
      <span class="contact-phone">
        <svg class="phone-icon" viewBox="0 0 20 22" aria-hidden="true"><path d="M5 1 L8 6 L6 8 C7 11 9 14 12 16 L14 14 L19 17 L17 21 C9 21 1 12 1 4 Z"/></svg>
        0492 837 514
      </span>
    </div>
  </section>
</main>
</body>
</html>
```